Membership Sales Page Web Design

We need a website designed to showcase the benefits of joining our online community of technology procurement professionals.

Our community has been around for a while and it's time for a refresh. Included in the brief is Verson 1.0 of the site. You can see the current version of the site @ brindlehub.com.

As part of the refresh, we've acquired a new primary domain name (brindle.com) and will be rolling out both a free and paid subscription model.

Because of this, there should be a strong call to sign (join now) infused within the site.

We would like to see site designs that are clean, flat and minimalistic in nature. Our membership colors are royal blue, grey, and white.

The final design should communicate networking and professional growth.

I'd be particularly interestedin seeing some flat website designs with a strong call to action. Here are some great examples for inspiration:

https://pivotlyst.com/
https://marrowkit.io/

Target Market(s)

vantage 400 companies

Number of Pages Required

1 page

Font styles to use
Sans Serif

Colors
0293ce
3276b5
ffffff

Requirements
Must have
• clean, minimalistic, fee
strong call to action
showcase our different membership levels
highlight the benefits of membership
Nice to have
• n/a
Should not have
• n/a

```html
<!DOCTYPE html>
<html lang="en">
<head>
<meta charset="utf-8">
<title>Brindle Membership</title>
<link href="https://fonts.googleapis.com/css2?family=Poppins:wght@400;500;600;700;800&display=swap" rel="stylesheet">
<style>
:root{
  --orange:#ff6a00;
  --blue:#0a78c5;
  --blue-soft:#d8effb;
  --ink:#111111;
  --text:#1f1f1f;
  --muted:#7a9bb5;
  --rule:#8a8f94;
  --bg:#ffffff;
}
*{box-sizing:border-box;margin:0;padding:0}
html,body{width:1200px;height:1200px;overflow:hidden;background:var(--bg)}
body{position:relative;font-family:'Poppins',sans-serif;color:var(--text)}
.abs{position:absolute}

.plan{position:absolute;top:54px;width:217px;height:350px;border:4px solid var(--blue-soft);border-radius:8px;background:#fff}
.plan--featured{top:46px;left:514px;width:216px;height:372px;border:4px solid var(--blue);box-shadow:0 10px 22px rgba(10,120,197,.18)}
.plan__badge{position:absolute;top:-13px;left:50px;width:112px;height:26px;border-radius:9px;background:var(--orange);color:#fff;font-size:10px;font-weight:600;letter-spacing:-.3px;text-align:center;line-height:26px}
.plan__title{position:absolute;top:28px;left:0;right:0;text-align:center;font-size:30px;font-weight:700;letter-spacing:-1px;color:var(--ink)}
.plan--featured .plan__title{top:22px}
.plan__rule{position:absolute;top:69px;left:23px;width:166px;height:2px;background:var(--orange)}
.plan--featured .plan__rule{top:71px}
.plan__features{position:absolute;top:104px;left:23px;list-style:none}
.plan--featured .plan__features{top:112px}
.plan__features li{display:flex;align-items:center;height:21px;font-size:13.5px;font-weight:500;letter-spacing:-.3px;color:var(--ink);white-space:nowrap}
.tick{width:13px;height:11px;margin-right:10px;flex:none}
.plan__price{position:absolute;top:237px;left:0;right:0;text-align:center;color:var(--blue);font-size:29px;font-weight:700;letter-spacing:-1px}
.plan__price span{font-size:14px;font-weight:400;color:var(--muted);letter-spacing:0;margin-left:4px}
.plan--featured .plan__price{top:258px}
.plan__cta{position:absolute;top:285px;left:38px;width:131px;height:40px;border:2px solid var(--orange);border-radius:6px;color:var(--orange);font-size:15px;font-weight:700;letter-spacing:-.6px;text-align:center;line-height:36px;background:#fff}
.plan--featured .plan__cta{top:307px;left:37px;background:var(--orange);color:#fff}

.benefit-nav{position:absolute;left:225px;top:560px;width:205px}
.benefit-nav__item{position:absolute;left:46px;font-size:13px;color:var(--ink);letter-spacing:-.2px;white-space:nowrap}
.benefit-nav__rule{position:absolute;left:0;width:205px;height:1px;background:var(--rule)}

.join__title{position:absolute;left:467px;top:515px;font-size:46px;font-weight:800;line-height:49px;letter-spacing:-2.5px;color:var(--ink)}
.join__bracket{position:absolute;left:719px;top:690px;width:31px;height:27px;border-top:1.5px solid var(--blue);border-right:1.5px solid var(--blue)}
.join__copy{position:absolute;left:471px;top:698px;width:265px;font-size:12.6px;line-height:19.3px;text-align:justify;letter-spacing:-.3px;color:var(--ink)}
.join__list{position:absolute;left:472px;top:891px;list-style:none}
.join__list li{display:flex;align-items:center;height:36.2px;font-size:13.6px;font-weight:600;letter-spacing:-.4px;color:var(--ink);white-space:nowrap}
.join__list .tick{margin-right:12px}

.join__photo{position:absolute;left:775px;top:525px;width:247px;height:490px;border-radius:120px 0 0 60px;background:linear-gradient(160deg,#5a3b2c 0%,#8a6450 30%,#d9cfc8 62%,#f4f2f1 85%,rgba(255,255,255,0) 100%)}
</style>
</head>
<body>

<svg width="0" height="0" class="abs" aria-hidden="true">
  <defs>
    <symbol id="tick" viewBox="0 0 13 11"><path d="M1.5 5.8 L5 9 L11.5 1.8" fill="none" stroke="#ff6a00" stroke-width="2.4" stroke-linecap="round" stroke-linejoin="round"/></symbol>
  </defs>
</svg>

<section class="plans">
  <article class="plan" style="left:275px">
    <h2 class="plan__title">Free.</h2>
    <div class="plan__rule"></div>
    <ul class="plan__features">
      <li><svg class="tick"><use href="#tick"/></svg>Free Membership</li>
      <li><svg class="tick"><use href="#tick"/></svg>Own E-mail address</li>
      <li><svg class="tick"><use href="#tick"/></svg>Gain valuable skills</li>
    </ul>
    <div class="plan__price">0$<span>/ Month</span></div>
    <div class="plan__cta">Select plan</div>
  </article>

  <article class="plan plan--featured">
    <div class="plan__badge">MOST POPULAR</div>
    <h2 class="plan__title">Standard.</h2>
    <div class="plan__rule"></div>
    <ul class="plan__features">
      <li><svg class="tick"><use href="#tick"/></svg>Daily News 24/7/365</li>
      <li><svg class="tick"><use href="#tick"/></svg>Ideas &amp; Themes</li>
      <li><svg class="tick"><use href="#tick"/></svg>Valuable tutorials</li>
      <li><svg class="tick"><use href="#tick"/></svg>Get Support</li>
    </ul>
    <div class="plan__price">19$<span>/ Month</span></div>
    <div class="plan__cta">Select plan</div>
  </article>

  <article class="plan" style="left:753px">
    <h2 class="plan__title">Plus.</h2>
    <div class="plan__rule"></div>
    <ul class="plan__features" style="top:103px">
      <li><svg class="tick"><use href="#tick"/></svg>1 year premium access</li>
      <li><svg class="tick"><use href="#tick"/></svg>Videos &amp; Tutorials</li>
      <li><svg class="tick"><use href="#tick"/></svg>Live Chats</li>
      <li><svg class="tick"><use href="#tick"/></svg>Great community</li>
      <li><svg class="tick"><use href="#tick"/></svg>Support</li>
    </ul>
    <div class="plan__price">99$<span>/ Month</span></div>
    <div class="plan__cta">Select plan</div>
  </article>
</section>

<nav class="benefit-nav">
  <div class="benefit-nav__item" style="top:11px">Vendor-free Discussion</div>
  <div class="benefit-nav__rule" style="top:53px"></div>
  <div class="benefit-nav__item" style="top:79px">Forums</div>
  <div class="benefit-nav__rule" style="top:117px"></div>
  <div class="benefit-nav__item" style="top:147px">Vendor Scorecards</div>
  <div class="benefit-nav__rule" style="top:187px"></div>
  <div class="benefit-nav__item" style="top:214px">Document Library</div>
  <div class="benefit-nav__rule" style="top:255px"></div>
  <div class="benefit-nav__item" style="top:282px">Education Center</div>
  <div class="benefit-nav__rule" style="top:322px"></div>
  <div class="benefit-nav__item" style="top:349px">Brindle Events</div>
  <div class="benefit-nav__rule" style="top:390px"></div>
  <div class="benefit-nav__item" style="top:417px">Certification</div>
  <div class="benefit-nav__rule" style="top:460px"></div>
  <div class="benefit-nav__item" style="top:485px">Career Center</div>
</nav>

<section class="join">
  <h1 class="join__title">Become<br>a member<br>today!</h1>
  <div class="join__bracket"></div>
  <p class="join__copy">If you’re the person responsible for negotiating and managing contracts with vendors of technology products and services, Brindle membership is for you. It will enhance your performance and facilitate your proessional growth while you network with others to advance the art and science of technology procurement.</p>
  <ul class="join__list">
    <li><svg class="tick"><use href="#tick"/></svg>Work Smart</li>
    <li><svg class="tick"><use href="#tick"/></svg>Do Better Deals</li>
    <li><svg class="tick"><use href="#tick"/></svg>Gain valuable skills</li>
    <li><svg class="tick"><use href="#tick"/></svg>Advance your career</li>
    <li><svg class="tick"><use href="#tick"/></svg>Counter vendor ploys</li>
    <li><svg class="tick"><use href="#tick"/></svg>Save time, money and aggravition</li>
    <li><svg class="tick"><use href="#tick"/></svg>Interact with your pers about vendors</li>
    <li><svg class="tick"><use href="#tick"/></svg>Share working solutions to real situations</li>
  </ul>
  <div class="join__photo" role="img" aria-label="Photo of a smiling professional woman with glasses holding a tablet"></div>
</section>

</body>
</html>
```